Corporate Template

Looking for a set of corporate slides to be made which contain multiple different slides and orientations. Looking for at least 8 to 10 different master pages plus a Coversheet and closeout page. Incorporating a color palate similar to our logo coloring is preferred.
I have attached a logo.
I like the calm pixel nook designs best so far. They seem to fit what I'm looking for in terms of visual appearance.
Reason: I'm trying to allow time for a couple new designers to incorporate some changes I requested to their existing designs.

```html
<!DOCTYPE html>
<html lang="en">
<head>
<meta charset="utf-8">
<title>Summit Neuro Labs – Corporate Slide Masters</title>
<link rel="stylesheet" href="https://fonts.googleapis.com/css2?family=Carlito:wght@400;700&display=swap">
<style>
:root{
  --brand-blue:#3a70b4;
  --white:#ffffff;
  --black:#000000;
  --dark-gray:#73758b;
  --mid-gray:#b9babb;
  --light-gray:#e5ecef;
  --orange:#f05322;
  --purple:#823e80;
  --green:#00892b;
  --text:#222222;
  --muted:#666666;
  --frame:#3a3a3a;
}
*{box-sizing:border-box;margin:0;padding:0}
html,body{width:1200px;height:880px;overflow:hidden;background:var(--white);font-family:'Carlito',sans-serif;color:var(--text)}
.sheet{position:absolute;left:24px;top:30px;display:grid;grid-template-columns:repeat(4,277px);grid-auto-rows:157px;column-gap:14px;row-gap:9px}
.slide{position:relative;border:1px solid var(--frame);background:var(--white);overflow:hidden}
.slide--blue{background:var(--brand-blue);color:var(--white)}
.footer{position:absolute;left:8px;bottom:4px;font-size:3.5px;color:#888}
.slide--blue .footer{color:#dce6f3}
.corner-mark{position:absolute;right:6px;bottom:4px;font-size:4px;font-weight:700;color:var(--brand-blue)}
.slide--blue .corner-mark{color:var(--white)}
.wordmark{font-weight:700;color:var(--brand-blue);text-align:center;letter-spacing:.5px}
.slide-title{position:absolute;left:10px;top:8px;font-size:11px;font-weight:700;color:var(--black)}
.subtitle{font-size:6px;color:var(--text)}
.lead{position:absolute;left:10px;top:32px;font-size:5.5px;color:var(--text)}
.body{position:absolute;left:10px;font-size:5px;line-height:1.35;color:var(--text)}
.heading-blue{color:var(--brand-blue);font-weight:700}
.bullets{list-style:none}
.bullets li{position:relative;padding-left:5px}
.bullets li::before{content:"•";position:absolute;left:0}
.bullets .l2{margin-left:6px}
.bullets .l2::before{content:"–"}
.bullets .l3{margin-left:12px}
.photo{position:absolute}
.cover-title{position:absolute;left:0;right:0;text-align:center}
.cover-title h1{font-size:15px;line-height:1.1;font-weight:700;color:#595959}
.cover-title p{font-size:5.5px;color:var(--muted);line-height:1.5}
.slide--blue .cover-title h1,.slide--blue .cover-title p{color:var(--white)}
.master-title{position:absolute;font-size:14px;font-weight:700;line-height:1.1;color:#1a1a1a}
.master-title span{display:block;font-size:5.5px;font-weight:400;margin-top:3px}
.chart{position:absolute}
.legend{position:absolute;font-size:4.5px;line-height:1.6}
.swatch{display:inline-block;width:5px;height:5px;vertical-align:middle;margin-right:2px}
.org-top{position:absolute;background:var(--brand-blue);color:var(--white);font-size:4px;font-weight:700;padding:2px 3px;line-height:1.3}
.org-cell{font-size:3.8px;line-height:1.3}
.grid-table{position:absolute;border-collapse:collapse;font-size:4px}
.grid-table td,.grid-table th{padding:1.5px 3px;text-align:left}
.chevron{position:absolute;height:11px;font-size:4px;font-weight:700;color:var(--white);padding:1.5px 3px;line-height:1.2;clip-path:polygon(0 0,88% 0,100% 50%,88% 100%,0 100%)}
.thank{position:absolute;left:10px;top:8px;font-size:12px;font-weight:700}
.spec-chip{position:absolute;width:26px;height:18px}
.spec-label{position:absolute;font-size:3.8px;line-height:1.3}
</style>
</head>
<body>
<main class="sheet">

  <!-- 1 Cover, white -->
  <section class="slide">
    <div class="wordmark" style="position:absolute;left:0;right:0;top:22px;font-size:14px">SUMMIT NEURO LABS</div>
    <div style="position:absolute;left:98px;width:80px;top:44px;height:1px;background:var(--mid-gray)"></div>
    <div class="cover-title" style="top:85px">
      <h1>Title<br>(46 pt. Calibri bold)</h1>
      <p>Subtitle (18 pt. Calibri)<br>Speaker's name / Month day, 2013</p>
    </div>
    <p class="footer">© 2013 Summit Neuro Labs | 100 Example Drive, Suite 1, Sampletown</p>
  </section>

  <!-- 2 Photo title -->
  <section class="slide">
    <div class="photo" role="img" aria-label="Doctor in a white coat holding a tablet" style="left:0;top:0;right:0;bottom:14px;background:linear-gradient(100deg,#d9d6d2 0%,#f3f2f0 45%,#c9c4be 100%)"></div>
    <h2 class="master-title" style="left:10px;top:62px">Click to edit master<br>title style<span>Click to edit master subtitle style</span></h2>
    <p class="footer">© 2013 Summit Neuro Labs | 100 Example Drive, Suite 1, Sampletown</p>
    <span class="corner-mark">SUMMIT NEURO LABS</span>
  </section>

  <!-- 3 Quote -->
  <section class="slide slide--blue">
    <p style="position:absolute;left:10px;top:10px;font-size:12.5px;font-weight:700;line-height:1.2">“Insert quote here”<br>(40 pt. Calibri bold)</p>
    <p style="position:absolute;left:10px;top:100px;font-size:5.5px;line-height:1.8">Quoted person's name, title and company<br>(18 pt. Calibri)</p>
    <p class="footer">© 2013 Summit Neuro Labs | 100 Example Drive, Suite 1, Sampletown</p>
    <span class="corner-mark">SNL</span>
  </section>

  <!-- 4 Text -->
  <section class="slide">
    <h2 class="slide-title">Title (28 pt. Calibri bold)</h2>
    <p class="subtitle" style="position:absolute;left:10px;top:24px">Subtitle (18 pt. Calibri)</p>
    <div class="body" style="top:36px;width:250px">
      <p class="heading-blue" style="font-size:5.5px">Heading (18 pt. Calibri bold SNL blue)</p>
      <p>Body copy (16 pt. Calibri)</p>
      <ul class="bullets">
        <li>Put your first-level bullet here. Try to keep bullet lists simple. (14 pt. Calibri)</li>
        <li class="l2">Put your second-level bullet here. Use no more than you need to explain your point. (14 pt. Calibri)</li>
        <li class="l3">Put your third-level of copy here. Use no more than you need to explain your point. (14 pt. Calibri)</li>
      </ul>
    </div>
    <p class="footer">© 2013 Summit Neuro Labs | 100 Example Drive, Suite 1, Sampletown</p>
    <span class="corner-mark">SNL</span>
  </section>

  <!-- 5 Cover, blue -->
  <section class="slide slide--blue">
    <div class="wordmark" style="position:absolute;left:0;right:0;top:24px;font-size:14px;color:var(--white)">SUMMIT NEURO LABS</div>
    <div style="position:absolute;left:98px;width:80px;top:46px;height:1px;background:#8fb0da"></div>
    <div class="cover-title" style="top:85px">
      <h1>Title<br>(46 pt. Calibri bold)</h1>
      <p>Subtitle (18 pt. Calibri)<br>Speaker's name / Month day, 2013</p>
    </div>
    <p class="footer">© 2013 Summit Neuro Labs | 100 Example Drive, Suite 1, Sampletown</p>
  </section>

  <!-- 6 Photo title 2 -->
  <section class="slide">
    <div class="photo" role="img" aria-label="Clinician reviewing a printed EEG chart" style="left:0;top:0;right:0;bottom:14px;background:linear-gradient(120deg,#e6dccf 0%,#d2b89a 40%,#f1ece4 75%,#cfc4b6 100%)"></div>
    <h2 class="master-title" style="left:138px;top:80px">Click to edit master<br>title style<span>Click to edit master subtitle style</span></h2>
    <p class="footer">© 2013 Summit Neuro Labs | 100 Example Drive, Suite 1, Sampletown</p>
    <span class="corner-mark">SUMMIT NEURO LABS</span>
  </section>

  <!-- 7 Text with image -->
  <section class="slide">
    <h2 class="slide-title">Title (28 pt. Calibri bold)</h2>
    <p class="subtitle" style="position:absolute;left:10px;top:24px">Subtitle (18 pt. Calibri)</p>
    <div class="body" style="top:38px;width:100px">
      <p class="heading-blue" style="font-size:5.5px">Heading (18 pt. Calibri bold<br>SNL blue)</p>
      <p>Body copy (16 pt. Calibri)</p>
      <ul class="bullets">
        <li>Put your first-level bullet here. (14 pt. Calibri)</li>
        <li class="l2">Put your second-level bullet here. (14 pt. Calibri)</li>
        <li class="l3">Put your third-level of copy here. (14 pt. Calibri)</li>
      </ul>
    </div>
    <div class="photo" role="img" aria-label="EEG recording trace on grid paper" style="left:128px;top:36px;width:136px;height:98px;background:linear-gradient(180deg,#dfeee0,#c9dfd0)"></div>
    <p class="footer">© 2013 Summit Neuro Labs | 100 Example Drive, Suite 1, Sampletown</p>
    <span class="corner-mark">SNL</span>
  </section>

  <!-- 8 Executive biography -->
  <section class="slide">
    <h2 class="slide-title">Executive Biography</h2>
    <p class="heading-blue" style="position:absolute;left:10px;top:23px;font-size:5.5px">Name here (18 pt. Calibri bold SNL blue)</p>
    <p style="position:absolute;left:10px;top:31px;font-size:5px;font-weight:700">Title here (16 pt. Calibri bold value of black)</p>
    <div style="position:absolute;left:10px;top:41px;width:50px;height:60px;border:1px solid var(--mid-gray);font-size:5px;display:flex;align-items:center;justify-content:center;text-align:center">Click icon to add picture</div>
    <div class="wordmark" style="position:absolute;left:6px;top:108px;width:58px;font-size:5.5px">SUMMIT NEURO LABS</div>
    <div class="body" style="left:68px;top:40px;width:200px">
      <p>Put your biography description here. Put your biography description here. Put your biography description here. Put your biography description here. Put your biography description here. Put your biography description here. Put your biography description here.</p>
      <ul class="bullets">
        <li>Succinct Achievements. Put your first-level bullet here. (14 pt. Calibri)</li>
        <li class="l2">Put your second-level bullet here. (14 pt. Calibri)</li>
        <li class="l3">Put your third-level of copy here. (14 pt. Calibri)</li>
      </ul>
    </div>
    <p class="footer">© 2013 Summit Neuro Labs | 100 Example Drive, Suite 1, Sampletown</p>
    <span class="corner-mark">SNL</span>
  </section>

  <!-- 9 Org chart expanded -->
  <section class="slide">
    <h2 class="slide-title">Organization chart style (expanded)</h2>
    <p class="body" style="top:34px">Box size and quantity may vary, but colors must be maintained.</p>
    <div class="org-top" style="left:12px;top:46px;width:70px">Insert Name<br>Title goes here (12 pt. Calibri bold)</div>
    <svg class="chart" style="left:10px;top:60px" width="260" height="12" viewBox="0 0 260 12"><path d="M37 0V4M20 4H245M20 4V12M58 4V12M98 4V12M138 4V12M178 4V12M218 4V12" stroke="#999" stroke-width=".6" fill="none"/></svg>
    <table class="grid-table" style="left:12px;top:70px;width:250px">
      <tr style="background:var(--dark-gray);color:var(--white);font-weight:700"><td>This level is all the same color</td><td>12 pt. Calibri bold</td><td>12 pt. Calibri bold</td><td>12 pt. Calibri bold</td><td>12 pt. Calibri bold</td><td>12 pt. Calibri bold</td></tr>
      <tr style="background:var(--light-gray)"><td>Name<br>Title</td><td>11 pt.<br>Calibri</td><td>11 pt.<br>Calibri</td><td>11 pt.<br>Calibri</td><td>11 pt.<br>Calibri</td><td>11 pt.<br>Calibri</td></tr>
      <tr><td>Name<br>Title</td><td>11 pt.<br>Calibri</td><td>11 pt.<br>Calibri</td><td>11 pt.<br>Calibri</td><td>11 pt.<br>Calibri</td><td>11 pt.<br>Calibri</td></tr>
      <tr style="background:var(--light-gray)"><td>Name<br>Title</td><td>11 pt.<br>Calibri</td><td>11 pt.<br>Calibri</td><td>11 pt.<br>Calibri</td><td>11 pt.<br>Calibri</td><td>11 pt.<br>Calibri</td></tr>
      <tr><td>Name<br>Title</td><td>11 pt.<br>Calibri</td><td>11 pt.<br>Calibri</td><td>11 pt.<br>Calibri</td><td>11 pt.<br>Calibri</td><td>11 pt.<br>Calibri</td></tr>
    </table>
    <p class="footer">© 2013 Summit Neuro Labs | 100 Example Drive, Suite 1, Sampletown</p>
    <span class="corner-mark">SNL</span>
  </section>

  <!-- 10 Flow chart -->
  <section class="slide">
    <h2 class="slide-title">Flow chart style</h2>
    <p class="body" style="top:34px">Box size and quantity may vary, but colors must be maintained.</p>
    <div class="chevron" style="left:12px;top:48px;width:48px;background:var(--brand-blue)">12 pt. bold<br>Calibri</div>
    <div class="chevron" style="left:62px;top:48px;width:48px;background:var(--dark-gray)">12 pt. bold<br>Calibri</div>
    <div class="chevron" style="left:112px;top:48px;width:48px;background:var(--dark-gray)">12 pt. bold<br>Calibri</div>
    <div class="chevron" style="left:162px;top:48px;width:48px;background:var(--dark-gray)">12 pt. bold<br>Calibri</div>
    <div class="chevron" style="left:212px;top:48px;width:48px;background:var(--dark-gray)">12 pt. bold<br>Calibri</div>
    <ul class="bullets body" style="left:12px;top:64px;width:45px;font-size:3.8px"><li>A percentage of or solid black may be used</li><li>11 pt. Calibri</li></ul>
    <ul class="bullets body" style="left:62px;top:64px;width:45px;font-size:3.8px"><li>A percentage of or solid black may be used</li><li>11 pt. Calibri</li></ul>
    <ul class="bullets body" style="left:112px;top:64px;width:45px;font-size:3.8px"><li>A percentage of or solid black may be used</li><li>11 pt. Calibri</li></ul>
    <ul class="bullets body" style="left:162px;top:64px;width:45px;font-size:3.8px"><li>A percentage of or solid black may be used</li><li>11 pt. Calibri</li></ul>
    <ul class="bullets body" style="left:212px;top:64px;width:45px;font-size:3.8px"><li>A percentage of or solid black may be used</li><li>11 pt. Calibri</li></ul>
    <p class="footer">© 2013 Summit Neuro Labs | 100 Example Drive, Suite 1, Sampletown</p>
    <span class="corner-mark">SNL</span>
  </section>

  <!-- 11 Pie chart -->
  <section class="slide">
    <h2 class="slide-title">Pie chart sample</h2>
    <div class="body" style="top:30px;width:115px">
      <p>Segments may vary, but only use SNL blue, one accent color and the permitted values of black.</p>
      <ul class="bullets"><li>All other copy is black.</li><li>Bullets are 14 pt. Calibri.</li><li>Pie segment percentages are 14 pt. Calibri.</li><li>Pie legend is 14 pt. Calibri.</li></ul>
    </div>
    <svg class="chart" style="left:130px;top:38px" width="100" height="80" viewBox="0 0 100 80">
      <path d="M50 40L50 12A28 28 0 1 1 35 63.6Z" fill="var(--brand-blue)"/>
      <path d="M50 40L35 63.6A28 28 0 0 1 24.7 28.1Z" fill="var(--purple)"/>
      <path d="M50 40L24.7 28.1A28 28 0 0 1 36.5 15.5Z" fill="var(--mid-gray)"/>
      <path d="M50 40L36.5 15.5A28 28 0 0 1 50 12Z" fill="var(--dark-gray)"/>
      <g font-size="4.5" fill="#222"><text x="84" y="47">59%</text><text x="22" y="75">23%</text><text x="6" y="26">10%</text><text x="37" y="8">8%</text></g>
    </svg>
    <div class="legend" style="left:228px;top:48px">
      <div><span class="swatch" style="background:var(--brand-blue)"></span>SNL Blue</div>
      <div><span class="swatch" style="background:var(--purple)"></span>Accent color</div>
      <div><span class="swatch" style="background:var(--mid-gray)"></span>Value of black</div>
      <div><span class="swatch" style="background:var(--dark-gray)"></span>Value of black</div>
    </div>
    <p class="footer">© 2013 Summit Neuro Labs | 100 Example Drive, Suite 1, Sampletown</p>
    <span class="corner-mark">SNL</span>
  </section>

  <!-- 12 Bar chart -->
  <section class="slide">
    <h2 class="slide-title">Bar chart sample</h2>
    <p class="body" style="top:30px">Data may vary, but only use SNL blue, one accent color and the permitted values of black.</p>
    <svg class="chart" style="left:14px;top:40px" width="250" height="100" viewBox="0 0 250 100">
      <g stroke="#ddd" stroke-width=".5"><path d="M14 5H245M14 19H245M14 33H245M14 47H245M14 61H245"/></g>
      <path d="M14 75H245" stroke="#888" stroke-width=".6"/>
      <g font-size="4.5" fill="#333"><text x="6" y="7">5</text><text x="6" y="21">4</text><text x="6" y="35">3</text><text x="6" y="49">2</text><text x="6" y="63">1</text><text x="6" y="77">0</text></g>
      <g fill="var(--brand-blue)"><rect x="26" y="55.4" width="8" height="19.6"/><rect x="72" y="37.2" width="8" height="37.8"/><rect x="118" y="17.6" width="8" height="57.4"/><rect x="164" y="9.2" width="8" height="65.8"/><rect x="210" y="37.2" width="8" height="37.8"/></g>
      <g fill="var(--purple)"><rect x="35" y="44.2" width="8" height="30.8"/><rect x="81" y="49.8" width="8" height="25.2"/><rect x="127" y="26" width="8" height="49"/><rect x="173" y="24.6" width="8" height="50.4"/><rect x="219" y="16.2" width="8" height="58.8"/></g>
      <g fill="var(--mid-gray)"><rect x="44" y="23.2" width="8" height="51.8"/><rect x="90" y="45.6" width="8" height="29.4"/><rect x="136" y="63.8" width="8" height="11.2"/><rect x="182" y="16.2" width="8" height="58.8"/><rect x="228" y="26" width="8" height="49"/></g>
      <g font-size="4.5" fill="#333"><text x="32" y="82">2009</text><text x="78" y="82">2010</text><text x="124" y="82">2011</text><text x="170" y="82">2012</text><text x="216" y="82">2013</text></g>
    </svg>
    <div class="legend" style="left:50px;top:130px;display:flex;gap:10px">
      <span><span class="swatch" style="background:var(--brand-blue)"></span>SNL Blue (14 pt. Calibri)</span>
      <span><span class="swatch" style="background:var(--purple)"></span>Accent color</span>
      <span><span class="swatch" style="background:var(--mid-gray)"></span>Value of black</span>
    </div>
    <p class="footer">© 2013 Summit Neuro Labs | 100 Example Drive, Suite 1, Sampletown</p>
    <span class="corner-mark">SNL</span>
  </section>

  <!-- 13 Table -->
  <section class="slide">
    <h2 class="slide-title">Table style</h2>
    <p class="body" style="top:30px">Columns and rows may be added, but colors must be maintained.</p>
    <table class="grid-table" style="left:10px;top:48px;width:257px">
      <tr style="font-weight:700;color:var(--white)"><td></td><td style="background:var(--brand-blue)">Heading</td><td style="background:var(--brand-blue)">Heading</td><td style="background:var(--brand-blue)">Heading</td><td style="background:var(--brand-blue)">Heading</td></tr>
      <tr style="background:var(--mid-gray)"><td>12 pt. Calibri</td><td>Content</td><td>Content</td><td>Content</td><td>Content</td></tr>
      <tr><td>Content</td><td>Content</td><td>Content</td><td>Content</td><td>Content</td></tr>
      <tr style="background:var(--light-gray)"><td>Content</td><td>Content</td><td>Content</td><td>Content</td><td>Content</td></tr>
      <tr><td>Content</td><td>Content</td><td>Content</td><td>Content</td><td>Content</td></tr>
      <tr style="background:var(--light-gray);color:var(--brand-blue)"><td>12 pt. Calibri bold SNL blue</td><td>Content</td><td>Content</td><td>Content</td><td>Content</td></tr>
      <tr><td>Content</td><td>Content</td><td>Content</td><td>Content</td><td>Content</td></tr>
    </table>
    <p class="footer">© 2013 Summit Neuro Labs | 100 Example Drive, Suite 1, Sampletown</p>
    <span class="corner-mark">SNL</span>
  </section>

  <!-- 14 Org chart condensed -->
  <section class="slide">
    <h2 class="slide-title">Organisation chart style (condensed)</h2>
    <p class="body" style="top:30px">Box size and quantity may vary, but colors must be maintained.</p>
    <div class="org-top" style="left:12px;top:38px;width:84px">Insert Name<br>Title goes here (12 pt. Calibri bold)</div>
    <svg class="chart" style="left:10px;top:51px" width="260" height="80" viewBox="0 0 260 80">
      <path d="M30 0V4M15 4H235M15 4V7M65 4V7M115 4V7M165 4V7M215 4V7" stroke="#999" stroke-width=".6" fill="none"/>
      <path d="M6 15V76M56 15V76M106 15V76M156 15V76M206 15V76" stroke="#999" stroke-width=".6" fill="none"/>
      <path d="M6 27H10M6 45H10M6 65H10M56 27H60M56 45H60M56 65H60M106 27H110M106 45H110M106 65H110M156 27H160M156 45H160M156 65H160M206 27H210M206 45H210M206 65H210" stroke="#999" stroke-width=".6"/>
    </svg>
    <div class="org-cell" style="position:absolute;left:12px;top:58px;width:44px;background:var(--dark-gray);color:#fff;font-weight:700;padding:1px 2px">This level is all the same color</div>
    <div class="org-cell" style="position:absolute;left:62px;top:58px;width:44px;background:var(--dark-gray);color:#fff;font-weight:700;padding:1px 2px">12 pt.<br>Calibri Bold</div>
    <div class="org-cell" style="position:absolute;left:112px;top:58px;width:44px;background:var(--dark-gray);color:#fff;font-weight:700;padding:1px 2px">12 pt.<br>Calibri Bold</div>
    <div class="org-cell" style="position:absolute;left:162px;top:58px;width:44px;background:var(--dark-gray);color:#fff;font-weight:700;padding:1px 2px">12 pt.<br>Calibri Bold</div>
    <div class="org-cell" style="position:absolute;left:212px;top:58px;width:44px;background:var(--dark-gray);color:#fff;font-weight:700;padding:1px 2px">12 pt.<br>Calibri Bold</div>
    <div class="org-cell" style="position:absolute;left:22px;top:75px">Name<br>Title<br><br><br>11 pt.<br>Calibri<br><br><br>11 pt.<br>Calibri</div>
    <div class="org-cell" style="position:absolute;left:72px;top:75px">Name<br>Title<br><br><br>11 pt.<br>Calibri<br><br><br>11 pt.<br>Calibri</div>
    <div class="org-cell" style="position:absolute;left:122px;top:75px">Name<br>Title<br><br><br>11 pt.<br>Calibri<br><br><br>11 pt.<br>Calibri</div>
    <div class="org-cell" style="position:absolute;left:172px;top:75px">Name<br>Title<br><br><br>11 pt.<br>Calibri<br><br><br>11 pt.<br>Calibri</div>
    <div class="org-cell" style="position:absolute;left:222px;top:75px">Name<br>Title<br><br><br>11 pt.<br>Calibri<br><br><br>11 pt.<br>Calibri</div>
    <p class="footer">© 2013 Summit Neuro Labs | 100 Example Drive, Suite 1, Sampletown</p>
    <span class="corner-mark">SNL</span>
  </section>

  <!-- 15 Line chart -->
  <section class="slide">
    <h2 class="slide-title">Line chart sample</h2>
    <p class="body" style="top:30px">Data may vary, but only use SNL blue, one accent color and the permitted values of black.</p>
    <svg class="chart" style="left:8px;top:40px" width="260" height="90" viewBox="0 0 260 90">
      <g stroke="#e3e3e3" stroke-width=".5"><path d="M12 5H250M12 18H250M12 31H250M12 44H250M12 57H250"/></g>
      <path d="M12 70H250" stroke="#888" stroke-width=".6"/>
      <g font-size="4.5" fill="#333"><text x="4" y="7">5</text><text x="4" y="20">4</text><text x="4" y="33">3</text><text x="4" y="46">2</text><text x="4" y="59">1</text><text x="4" y="72">0</text></g>
      <polyline points="30,50.5 80,31 130,15.4 180,7.6 230,33.6" fill="none" stroke="var(--purple)" stroke-width="1.1"/>
      <polyline points="30,41.4 80,46.6 130,27.1 180,21.9 230,14.1" fill="none" stroke="var(--mid-gray)" stroke-width="1.1"/>
      <polyline points="30,21.9 80,40.1 130,59.6 180,14.1 230,28.4" fill="none" stroke="var(--brand-blue)" stroke-width="1.1"/>
      <g font-size="4.5" fill="#333"><text x="24" y="78">2007</text><text x="74" y="78">2008</text><text x="124" y="78">2009</text><text x="174" y="78">2010</text><text x="224" y="78">2011</text></g>
    </svg>
    <div class="legend" style="left:30px;top:128px;display:flex;gap:14px">
      <span><span class="swatch" style="background:var(--purple);height:1.5px"></span>Accent color</span>
      <span><span class="swatch" style="background:var(--mid-gray);height:1.5px"></span>Value of black</span>
      <span><span class="swatch" style="background:var(--brand-blue);height:1.5px"></span>SNL blue / 14 pt. Calibri</span>
    </div>
    <p class="footer">© 2013 Summit Neuro Labs | 100 Example Drive, Suite 1, Sampletown</p>
    <span class="corner-mark">SNL</span>
  </section>

  <!-- 16 Chart with bullets -->
  <section class="slide">
    <h2 class="slide-title">Chart style with bulleted copy</h2>
    <p class="body" style="top:30px">Box size and quantity may vary, but colors must be maintained.</p>
    <div class="chevron" style="left:10px;top:48px;width:86px;background:var(--dark-gray);padding-top:3.5px">Example: Attend these sessions</div>
    <div class="chevron" style="left:96px;top:48px;width:86px;background:var(--dark-gray);padding-top:3.5px">12 pt. Calibri bold</div>
    <div class="chevron" style="left:182px;top:48px;width:86px;background:var(--dark-gray);padding-top:3.5px">12 pt. Calibri bold</div>
    <ul class="bullets body" style="left:14px;top:64px;width:78px;font-size:3.8px"><li>11 pt. Calibri</li><li>Example</li><li>Example</li></ul>
    <ul class="bullets body" style="left:100px;top:64px;width:78px;font-size:3.8px"><li>11 pt. Calibri</li><li>Example</li><li>Example</li></ul>
    <ul class="bullets body" style="left:186px;top:64px;width:80px;font-size:3.8px"><li>11 pt. Calibri</li><li>Example: Visit our website/feed at &lt;insert URL here&gt;</li><li>Example: Download the whitepaper at &lt;insert URL here&gt;</li></ul>
    <div class="chevron" style="left:10px;top:113px;width:256px;background:var(--brand-blue);clip-path:polygon(0 0,97% 0,100% 50%,97% 100%,0 100%);padding-top:3.5px">Example: Your feedback is important to us. Please take a few minutes to complete the session survey.</div>
    <p class="footer">© 2013 Summit Neuro Labs | 100 Example Drive, Suite 1, Sampletown</p>
    <span class="corner-mark">SNL</span>
  </section>

  <!-- 17 Questions -->
  <section class="slide">
    <h2 class="slide-title" style="font-size:12px">Questions</h2>
    <div class="photo" role="img" aria-label="Blue stethoscope shaped like a question mark" style="left:88px;top:26px;width:100px;height:100px;border-radius:40px;background:radial-gradient(circle,#8b9fd6 0%,#c5cfec 55%,#ffffff 75%)"></div>
    <p class="footer">© 2013 Summit Neuro Labs | 100 Example Drive, Suite 1, Sampletown</p>
    <span class="corner-mark">SNL</span>
  </section>

  <!-- 18 Thank you, blue -->
  <section class="slide slide--blue">
    <h2 class="thank">Thank you</h2>
    <p class="footer">© 2013 Summit Neuro Labs | 100 Example Drive, Suite 1, Sampletown</p>
    <span class="corner-mark">SNL</span>
  </section>

  <!-- 19 Thank you, photo -->
  <section class="slide">
    <div class="photo" role="img" aria-label="Doctor's white coat with a stethoscope around the neck" style="left:0;top:0;right:0;bottom:0;background:linear-gradient(90deg,#dfe5ec 0%,#f7f8fa 35%,#eef1f4 60%,#b9d3ea 100%)"></div>
    <h2 class="thank" style="color:var(--black)">Thank you</h2>
    <div style="position:absolute;right:4px;bottom:4px;background:var(--white);padding:3px 5px;font-size:5.5px;font-weight:700;color:var(--brand-blue)">SUMMIT NEURO LABS</div>
  </section>

  <!-- 20 Color specifications -->
  <section class="slide">
    <h2 class="slide-title" style="font-size:9px">Color</h2>
    <p style="position:absolute;right:8px;top:10px;font-size:4.5px;color:var(--orange)">Remove slide for all presentations</p>
    <p class="heading-blue" style="position:absolute;left:10px;top:35px;font-size:5px">Specifications</p>
    <p style="position:absolute;left:10px;top:46px;font-size:4.5px">Primary</p>
    <p style="position:absolute;left:68px;top:46px;font-size:4.5px">Neutral</p>
    <p style="position:absolute;left:184px;top:46px;font-size:4.5px">Accent</p>
    <div class="spec-chip" style="left:10px;top:53px;background:var(--brand-blue)"></div>
    <div class="spec-chip" style="left:38px;top:53px;background:var(--white);border:.5px solid #ccc"></div>
    <div class="spec-chip" style="left:68px;top:53px;background:var(--black)"></div>
    <div class="spec-chip" style="left:96px;top:53px;background:var(--dark-gray)"></div>
    <div class="spec-chip" style="left:124px;top:53px;background:var(--mid-gray)"></div>
    <div class="spec-chip" style="left:152px;top:53px;background:var(--light-gray)"></div>
    <div class="spec-chip" style="left:184px;top:53px;background:var(--orange)"></div>
    <div class="spec-chip" style="left:212px;top:53px;background:var(--purple)"></div>
    <div class="spec-chip" style="left:240px;top:53px;background:var(--green)"></div>
    <p class="spec-label" style="left:10px;top:74px">SNL blue<br>R = 58<br>G = 112<br>B = 180</p>
    <p class="spec-label" style="left:38px;top:74px">White<br>R = 255<br>G = 255<br>B = 255</p>
    <p class="spec-label" style="left:68px;top:74px">Black<br>R = 0<br>G = 0<br>B = 0</p>
    <p class="spec-label" style="left:96px;top:74px">Dark gray<br>R = 115<br>G = 117<br>B = 139</p>
    <p class="spec-label" style="left:124px;top:74px">Medium gray<br>R = 185<br>G = 186<br>B = 187</p>
    <p class="spec-label" style="left:152px;top:74px">Light gray<br>R = 229<br>G = 236<br>B = 239</p>
    <p class="spec-label" style="left:184px;top:74px">Orange<br>R = 240<br>G = 83<br>B = 34</p>
    <p class="spec-label" style="left:212px;top:74px">Purple<br>R = 130<br>G = 62<br>B = 128</p>
    <p class="spec-label" style="left:240px;top:74px">Green<br>R = 0<br>G = 137<br>B = 43</p>
    <span class="corner-mark">SNL</span>
  </section>

</main>
</body>
</html>
```